Penwick Mechanical Drain Cleaning and Jetting

We need to show our customers and potential customers that we now have the ability to perform Drain Cleaning, camera inspections, location services, and Hydro-Jetting Services. I would like the the colors to match the previous design.

```html
<!DOCTYPE html>
<html lang="en">
<head>
<meta charset="utf-8">
<title>Penwick Mechanical – Drain Cleaning and Jetting</title>
<link href="https://fonts.googleapis.com/css2?family=Roboto:ital,wght@0,400;0,500;0,700;0,900;1,700;1,900&display=swap" rel="stylesheet">
<style>
  :root {
    --page: #fcf2ef;
    --white: #ffffff;
    --green: #0b5c3e;
    --gold: #d3a74c;
    --gold-light: #e9c674;
    --ink: #1c1c1c;
  }
  * { margin: 0; padding: 0; box-sizing: border-box; }
  html, body { width: 927px; height: 1200px; overflow: hidden; }
  body { background: var(--page); font-family: "Roboto", Arial, sans-serif; position: relative; }

  .flyer { position: absolute; left: 68px; top: 88px; width: 791px; height: 1023px; background: var(--white); overflow: hidden; }
  .flyer-shapes { position: absolute; inset: 0; }

  .photo { position: absolute; left: 0; }
  .photo-drain { top: 176px; width: 330px; height: 317px; background: linear-gradient(135deg, #5c5d60, #3f4043 55%, #c96a2a); }
  .photo-camera { top: 432px; width: 340px; height: 155px; background: linear-gradient(120deg, #0e6f8c, #2aa6c4 50%, #0b3f55); }
  .photo-jetting { top: 617px; width: 340px; height: 155px; background: linear-gradient(120deg, #c9c9c4, #8c8f86 50%, #5e7c46); }
  .photo-location { top: 801px; width: 320px; height: 156px; background: linear-gradient(135deg, #e2c028, #b8a05a 45%, #8a8d91); }
  .photo-desk { top: 983px; width: 320px; height: 40px; background: linear-gradient(90deg, #e4e4e4, #bcbcbc); }
  .label-band { position: absolute; left: 0; width: 340px; height: 26px; background: var(--white); }

  .service-label { position: absolute; left: 0; width: 330px; text-align: center; color: var(--green); font-weight: 700; font-size: 15.5px; letter-spacing: 0.3px; line-height: 26px; }

  .headline { position: absolute; left: 68px; top: 55px; color: var(--white); font-size: 21.5px; font-weight: 400; line-height: 24.5px; letter-spacing: 0.2px; }
  .headline strong { font-weight: 700; }
  .subhead { position: absolute; left: 69px; top: 113px; width: 310px; color: var(--white); font-size: 19.3px; font-weight: 700; line-height: 23.6px; }

  .brand-badge { position: absolute; left: 537px; top: 79px; width: 204px; height: 204px; border-radius: 50%; background: var(--white); border-bottom: 3px solid var(--gold); display: flex; flex-direction: column; align-items: center; justify-content: center; text-align: center; }
  .brand-name { color: var(--green); font-weight: 900; font-size: 21px; line-height: 23px; text-transform: uppercase; }
  .brand-url { margin-top: 12px; color: var(--green); font-weight: 700; font-size: 13px; }

  .fixture { position: absolute; width: 100px; text-align: center; }
  .fixture-icon { width: 74px; height: 74px; margin: 0 auto; border-radius: 50%; background: var(--green); border: 4px solid var(--gold-light); display: flex; align-items: center; justify-content: center; }
  .fixture-icon svg { width: 38px; height: 38px; fill: none; stroke: var(--white); stroke-width: 2; stroke-linecap: round; stroke-linejoin: round; }
  .fixture-name { margin-top: 7px; font-size: 12.5px; font-weight: 500; line-height: 15.5px; color: var(--ink); }
  .fixture-wide { width: 320px; display: flex; align-items: center; gap: 16px; text-align: left; }
  .fixture-wide .fixture-icon { margin: 0; flex: none; }
  .fixture-wide .fixture-name { margin-top: 0; }

  .emblem-art { position: absolute; left: 366px; top: 818px; width: 156px; height: 148px; border-radius: 50%; background: radial-gradient(circle at 50% 50%, rgba(211,167,76,0.32), rgba(211,167,76,0.08) 70%, rgba(211,167,76,0) 72%); }
  .hours-number { position: absolute; left: 401px; top: 857px; color: var(--gold); font-size: 92px; font-weight: 900; font-style: italic; letter-spacing: -4px; line-height: 1; }
  .hours-word { position: absolute; left: 403px; top: 941px; color: var(--gold); font-size: 19px; font-weight: 900; font-style: italic; letter-spacing: 6px; line-height: 1; }
  .emergency-text { position: absolute; left: 511px; top: 873px; color: var(--gold); font-size: 25px; font-weight: 900; font-style: italic; line-height: 31px; letter-spacing: 0.5px; }
  .emergency-text span { display: block; }
  .emergency-text span:nth-child(2) { margin-left: -5px; }
  .emergency-text span:nth-child(3) { margin-left: -6px; }

  .contact-line { position: absolute; left: 329px; top: 993px; color: var(--green); font-size: 17.5px; font-weight: 700; letter-spacing: 0.3px; white-space: nowrap; }
  .contact-line .gap { display: inline-block; width: 22px; }
</style>
</head>
<body>
<main class="flyer">
  <div class="photo photo-drain" role="img" aria-label="Photo of workers in hi-vis gear cleaning a street drain with a hose"></div>
  <div class="photo photo-camera" role="img" aria-label="Photo of monitors showing camera inspection footage"></div>
  <div class="photo photo-jetting" role="img" aria-label="Photo of a hydro-jetting truck and crew on a street"></div>
  <div class="photo photo-location" role="img" aria-label="Photo of a hand with a magnifier over a map of building locations"></div>
  <div class="photo photo-desk" role="img" aria-label="Photo of a laptop edge on a desk"></div>
  <div class="label-band" style="top:405px"></div>
  <div class="label-band" style="top:589px"></div>
  <div class="label-band" style="top:774px"></div>
  <div class="label-band" style="top:957px"></div>

  <svg class="flyer-shapes" viewBox="0 0 791 1023" width="791" height="1023">
    <defs>
      <linearGradient id="topPhoto" x1="0" y1="0" x2="1" y2="0">
        <stop offset="0" stop-color="#2f241f"/>
        <stop offset="0.45" stop-color="#3d2f27"/>
        <stop offset="0.7" stop-color="#6b625c"/>
        <stop offset="1" stop-color="#4a5a80"/>
      </linearGradient>
    </defs>
    <path d="M276,250 C316,350 346,500 338,626 C331,760 286,900 176,1023 H791 V0 Z" fill="var(--gold)"/>
    <path d="M290,250 C330,350 360,500 352,626 C345,760 300,900 190,1023 H791 V0 Z" fill="var(--white)"/>
    <path d="M335,801 H791 V983 H226 C268,930 315,860 335,801 Z" fill="var(--green)"/>
    <path d="M0,178 C70,218 160,258 270,266 C370,272 470,258 560,234 L700,196 C740,182 768,166 791,146 V120 C720,160 620,200 520,222 C420,244 330,258 250,254 C150,246 70,214 0,176 Z" fill="var(--gold)"/>
    <path d="M0,0 H791 V120 C720,160 620,200 520,222 C420,244 330,258 250,254 C150,246 70,214 0,170 Z" fill="url(#topPhoto)" role="img" aria-label="Photo of a plumber in gloves and mask servicing a drain line under a sink"/>
  </svg>

  <div class="service-label" style="top:405px">DRAIN CLEANING</div>
  <div class="service-label" style="top:589px">CAMERA INSPECTIONS</div>
  <div class="service-label" style="top:774px">HYDRO-JETTING SERVICES</div>
  <div class="service-label" style="top:957px; width:300px">LOCATION SERVICES</div>

  <h1 class="headline">HAVE YOU NSPECTED <strong>ALL</strong><br><strong>YOUR PLUMBING FIXTURES</strong></h1>
  <p class="subhead">New installations, service, and maintenance of all brands of equipment</p>

  <div class="brand-badge">
    <div class="brand-name">Penwick<br>Mechanical</div>
    <div class="brand-url">www.penwickmechanical.com</div>
  </div>

  <section class="fixtures">
    <div class="fixture" style="left:362px; top:313px"><div class="fixture-icon"><svg viewBox="0 0 40 40"><circle cx="20" cy="20" r="11"/><circle cx="20" cy="20" r="4"/><path d="M9 8h8M13 8v6"/></svg></div><div class="fixture-name">Lift<br>Stations</div></div>
    <div class="fixture" style="left:455px; top:313px"><div class="fixture-icon"><svg viewBox="0 0 40 40"><path d="M6 20h28c-2 7-8 10-14 10S8 27 6 20z"/><path d="M18 20V9a4 4 0 0 1 8 0v3M20 30v5"/></svg></div><div class="fixture-name">Sinks</div></div>
    <div class="fixture" style="left:552px; top:313px"><div class="fixture-icon"><svg viewBox="0 0 40 40"><path d="M7 8h26v24H7zM7 26h26M12 26l-2 6M20 26v6M28 26l2 6"/></svg></div><div class="fixture-name">Confined<br>Space</div></div>
    <div class="fixture" style="left:646px; top:313px"><div class="fixture-icon"><svg viewBox="0 0 40 40"><path d="M11 14h18v4H11zM13 18l2 16h10l2-16M20 14v-4a3 3 0 0 1 6 0"/></svg></div><div class="fixture-name">Drinking<br>Fountain</div></div>

    <div class="fixture" style="left:362px; top:442px"><div class="fixture-icon"><svg viewBox="0 0 40 40"><path d="M6 9h28v4H6zM14 13v6h12v-6M18 19v6l-4 6M22 19v6"/></svg></div><div class="fixture-name">Roof<br>Drains</div></div>
    <div class="fixture" style="left:455px; top:442px"><div class="fixture-icon"><svg viewBox="0 0 40 40"><path d="M8 12h16v20H8zM12 16v12M16 16v12M20 16v12M6 32h28M28 8v20"/></svg></div><div class="fixture-name">Sump<br>Pumps</div></div>
    <div class="fixture" style="left:552px; top:442px"><div class="fixture-icon"><svg viewBox="0 0 40 40"><ellipse cx="20" cy="21" rx="9" ry="12"/><ellipse cx="20" cy="22" rx="5" ry="7"/><circle cx="20" cy="7" r="2"/></svg></div><div class="fixture-name">Toilets<br>/Urinals</div></div>
    <div class="fixture" style="left:646px; top:442px"><div class="fixture-icon"><svg viewBox="0 0 40 40"><path d="M14 34V14a6 6 0 0 1 12 0v3M8 26h8M24 20h4M25 24v8M29 24v8"/></svg></div><div class="fixture-name">Faucets/<br>Shower</div></div>

    <div class="fixture" style="left:362px; top:571px"><div class="fixture-icon"><svg viewBox="0 0 40 40"><ellipse cx="17" cy="25" rx="11" ry="7"/><ellipse cx="17" cy="25" rx="5" ry="3"/><path d="M24 16l8-8M28 8h4v4"/></svg></div><div class="fixture-name">Floor and<br>Sink Drains</div></div>
    <div class="fixture" style="left:455px; top:571px"><div class="fixture-icon"><svg viewBox="0 0 40 40"><rect x="11" y="5" width="18" height="28" rx="3"/><circle cx="20" cy="13" r="4"/><path d="M15 24h10M16 33v3M24 33v3"/></svg></div><div class="fixture-name">Water<br>Heaters</div></div>
    <div class="fixture" style="left:552px; top:571px"><div class="fixture-icon"><svg viewBox="0 0 40 40"><path d="M6 12h14v12h14M6 18h8v12h20M26 6v12M30 6v12"/></svg></div><div class="fixture-name">Piping</div></div>
    <div class="fixture" style="left:646px; top:569px"><div class="fixture-icon"><svg viewBox="0 0 40 40"><path d="M8 6h8v22H8zM16 14h6v14M6 33c4-2 6 2 10 0s6 2 10 0 6 2 8 0"/><path d="M29 18c-3 4-4 6-4 8a4 4 0 0 0 8 0c0-2-1-4-4-8z"/></svg></div><div class="fixture-name">Water Main<br>Emergency<br>Service</div></div>

    <div class="fixture fixture-wide" style="left:372px; top:699px"><div class="fixture-icon"><svg viewBox="0 0 40 40"><path d="M20 36c-8-9-12-14-12-20a12 12 0 0 1 24 0c0 6-4 11-12 20z"/><path d="M15 12l10 10M25 12l-10 10"/></svg></div><div class="fixture-name">Backflow Prevention Devices<br>(testing, installation, &amp; service)</div></div>
  </section>

  <section class="emergency">
    <div class="emblem-art" role="img" aria-label="Gold clock dial with a curved arrow around the 24 hours figure"></div>
    <div class="hours-number">24</div>
    <div class="hours-word">HOURS</div>
    <div class="emergency-text"><span>EMERGENCY</span><span>SERVICE</span><span>AVAILABLE</span></div>
  </section>

  <p class="contact-line">TOLL FREE&nbsp; : &nbsp;1-800.GO.PENWICK<span class="gap"></span>616-555-0148</p>
</main>
</body>
</html>
```